KelvaNest - Home Income and Business Resources Platform

I am looking for a website template for a multi-purposed website. This website will feature:

1.) Website Directory with Ratings & comments on listings
2.) Company Blog
3.) Homepage with Content (see files for homepage mock)

I would like the Design to have a default width 1170px (wider then normal)

Of course I am looking for Pages for Listings to be designed.

Great looking BLOG Layout: http://journal.pixelvorn.example/html/blog.html

I would like 4 Versions of a Website Directory Listing "Box"
1.) Basic Listing Box
2.) Sponsored Listing Box
3.) Recommended Listing Box
4.) Stay Away From Listing Box

Information on the Listing Page (Like on a Category Page)
Site Name, Site URL, Website Image, # of Views, Rating and # of Comments

Information on the Listing Details Page:
Same as ABOVE + About website Description, Trovix Rank, Category Information

Decent looking examples is here: https://demos.quendaro.example/directory/computers/ and http://www.zibrankhub.example/.

I will include some sketches and screenshots of things I like/looking for. As designers,you have creative freedom and are encouraged to show this. This is Phase one of this project and winning designer is guaranteed to have future work for this project.

Target Market(s)

Directory, business, websites

Industry/Entity Type

Business

Font styles to use
Sans Serif

Colors

Designer to choose colors to be used in the design.

Requirements
Must have
• Professional yet clean look. The use of Icons & images
• Unique Look
Should not have
• Any exact copies of any examples I provided

```html
<!DOCTYPE html>
<html lang="en">
<head>
<meta charset="utf-8">
<title>KelvaNest – Home Income and Business Resources</title>
<link rel="stylesheet" href="https://fonts.googleapis.com/css2?family=Raleway:wght@200;300;400;500;600;700&family=Open+Sans:wght@400;600&display=swap">
<style>
:root{
  --page:#e6eef9;
  --blue:#1669d1;
  --blue-text:#1a6fd0;
  --link:#1893dd;
  --orange:#ff6a0d;
  --ink:#1d1d1d;
  --body:#555a60;
  --line:#d9dde3;
  --card-border:#a9c6ec;
  --white:#ffffff;
  --dark:#0d0d0d;
  --tab:#f2f2f2;
  --tab-dot:#dfe6f0;
}
*{box-sizing:border-box;margin:0;padding:0}
html,body{width:1200px;height:2329px;overflow:hidden}
body{background:var(--page);position:relative;font-family:"Open Sans",Arial,sans-serif;color:var(--body)}
.abs{position:absolute}

/* header */
.brand{left:47px;top:15px}
.brand-name{font-family:"Raleway",sans-serif;font-weight:700;font-size:19px;color:var(--blue-text);line-height:1}
.brand-tag{font-family:"Raleway",sans-serif;font-size:9px;color:#333;margin-top:3px}
.phone{right:44px;top:20px;font-family:"Raleway",sans-serif;font-size:15px;color:#555;display:flex;align-items:center;gap:6px}

.nav{left:43px;top:56px;width:1114px;height:35px;background:var(--blue);display:flex;align-items:center;padding:0 17px}
.nav a{font-family:"Raleway",sans-serif;font-weight:700;font-size:13px;color:var(--white);text-decoration:none;margin-right:16px}
.nav-social{margin-left:auto;display:flex;gap:13px}
.nav-social span{width:11px;height:11px;background:var(--white);border-radius:2px}

/* hero */
.hero{left:43px;top:109px;width:1114px;height:372px;background:linear-gradient(100deg,#2b2a2e 0%,#55565c 22%,#d9d6d2 40%,#eeeae6 62%,#c9c6c0 80%,#8d8d86 100%);box-shadow:0 10px 14px -8px rgba(60,80,110,.35)}
.hero-ring{left:86px;top:171px;width:294px;height:294px;border:2px solid var(--blue);border-radius:50%}
.hero-disc{left:93px;top:183px;width:280px;height:280px;background:var(--white);border-radius:50%;text-align:center;padding-top:30px}
.hero-title{font-family:"Raleway",sans-serif;font-size:19px;font-weight:500;color:var(--blue-text);line-height:26px}
.hero-rule{width:150px;height:1px;background:#bbb;margin:14px auto 12px}
.hero-text{font-size:11px;line-height:16px;color:#444;width:236px;margin:0 auto}
.btn{display:inline-block;font-family:"Raleway",sans-serif;font-weight:600;font-size:14px;color:var(--white);background:var(--orange);text-align:center;border-radius:2px}
.btn.blue{background:var(--blue)}
.hero-disc .btn{width:147px;height:37px;line-height:37px;margin-top:12px}

/* feature cards */
.feature{top:517px;width:349px;height:484px;background:linear-gradient(180deg,#fff 55%,#f1f6fd 100%);border:1px solid var(--card-border);border-radius:3px}
.feature-tab{position:absolute;left:117px;top:-2px;width:114px;height:88px;background:var(--tab);border-radius:0 0 57px 57px;box-shadow:0 5px 8px rgba(0,0,0,.18);display:flex;align-items:center;justify-content:center}
.feature-tab span{width:44px;height:44px;border-radius:50%;background:var(--tab-dot)}
.feature h2{position:absolute;left:13px;top:135px;font-family:"Raleway",sans-serif;font-weight:500;font-size:18px;color:var(--blue-text)}
.feature p{position:absolute;left:13px;top:170px;width:322px;font-size:12.5px;line-height:22.5px;color:var(--body);text-align:justify}
.feature .btn{position:absolute;left:13px;top:392px;width:155px;height:37px;line-height:37px}

/* posts */
.post{left:47px;width:680px;height:350px;background:var(--white)}
.post-photo{position:absolute;left:0;top:0;width:250px;height:350px}
.post-body{position:absolute;left:250px;top:0;width:430px;height:350px}
.post-title{position:absolute;left:0;width:430px;top:16px;text-align:center;font-family:"Raleway",sans-serif;font-size:21.5px;font-weight:500;color:var(--ink);line-height:26px}
.post-rule{position:absolute;left:188px;top:79px;width:52px;height:1px;background:#333}
.post-cat{position:absolute;left:0;width:430px;top:87px;text-align:center;font-size:11.5px;color:var(--link)}
.post-text{position:absolute;left:18px;top:122px;width:400px;font-size:13px;line-height:21.8px;color:var(--body)}
.post-meta{position:absolute;left:18px;top:251px;font-size:13px;color:#333}
.post-meta b{font-weight:400;color:var(--link)}
.post-divider{position:absolute;left:0;top:289px;width:430px;height:1px;background:var(--line)}
.post .btn{position:absolute;left:20px;top:300px;width:155px;height:37px;line-height:37px}
.post-stats{position:absolute;right:20px;top:311px;display:flex;gap:20px;font-size:12px;color:#333}
.post-stats span{display:flex;align-items:center;gap:6px}

/* sidebar */
.sidebar{left:775px;top:1040px;width:378px;height:1222px;background:var(--white)}
.avatar{position:absolute;left:117px;top:20px;width:142px;height:142px;border-radius:50%;border:4px solid #e0e0e0;background:radial-gradient(circle at 50% 45%,#c99a78 0%,#9b6b4c 45%,#d9d4cc 100%)}
.side-h{position:absolute;left:0;width:378px;text-align:center;font-family:"Raleway",sans-serif;font-size:21px;font-weight:500;color:var(--blue-text)}
.side-text{position:absolute;left:22px;top:208px;width:336px;font-size:12.5px;line-height:22px;color:var(--body);text-align:justify}
.side-rule{position:absolute;left:0;width:378px;height:1px;background:var(--line)}
.social{position:absolute;left:70px;top:425px;display:flex;gap:18px}
.social span{width:31px;height:31px;background:var(--link);border-radius:2px;position:relative}
.social span::after{content:"";position:absolute;left:10px;bottom:-7px;border:6px solid transparent;border-top-color:var(--link);border-bottom:0}
.follow{position:absolute;left:146px;top:472px;font-size:11px;color:#333}
.recent-photo{position:absolute;left:15px;top:573px;width:348px;height:120px;background:linear-gradient(90deg,#6e8a3a 0%,#9caf5a 35%,#c7a27f 60%,#b97a55 85%,#7e9a45 100%)}
.recent-title{position:absolute;left:0;width:378px;top:704px;text-align:center;font-family:"Raleway",sans-serif;font-weight:600;font-size:14px;color:var(--link)}
.recent-date{position:absolute;left:0;width:378px;top:733px;text-align:center;font-size:12.5px;color:#333}
.pager{position:absolute;left:160px;top:781px;display:flex;gap:4px}
.pager span{width:24px;height:24px;background:var(--orange);display:flex;align-items:center;justify-content:center}
.promo{position:absolute;left:18px;top:897px;width:343px;height:291px;background:var(--dark);padding:22px 16px}
.promo h3{font-family:"Raleway",sans-serif;font-weight:200;font-size:46px;line-height:50px;color:var(--white)}
.promo p{margin-top:20px;font-size:13px;line-height:20px;color:var(--white)}

/* footer */
.footer-rule{left:0;top:2288px;width:1200px;height:1px;background:var(--blue)}
.footer{left:43px;top:2297px;width:1114px;display:flex;align-items:center;font-size:11.5px;color:#555}
.footer-social{display:flex;gap:8px;margin-right:30px}
.footer-social span{width:9px;height:9px;background:#666;border-radius:1px}
.footer a{color:#555;text-decoration:none;margin-right:16px}
.copy{margin-left:auto}
</style>
</head>
<body>

<header>
  <div class="abs brand">
    <div class="brand-name">KelvaNest</div>
    <div class="brand-tag">Home Income and Business Resources</div>
  </div>
  <div class="abs phone">
    <svg width="13" height="13" viewBox="0 0 24 24"><path fill="#1a6fd0" d="M6.6 10.8a15.1 15.1 0 0 0 6.6 6.6l2.2-2.2a1 1 0 0 1 1-.25 11.4 11.4 0 0 0 3.6.6 1 1 0 0 1 1 1V20a1 1 0 0 1-1 1A17 17 0 0 1 3 4a1 1 0 0 1 1-1h3.5a1 1 0 0 1 1 1c0 1.25.2 2.45.6 3.6a1 1 0 0 1-.25 1z"/></svg>
    0800-000-000-000
  </div>
  <nav class="abs nav">
    <a href="#">HOME</a><a href="#">ABOUT</a><a href="#">PAGE TEMPLATES</a><a href="#">SHORTCODES</a><a href="#">SHOP PAGE</a><a href="#">CONTACT</a>
    <div class="nav-social"><span></span><span></span><span></span></div>
  </nav>
</header>

<section class="abs hero" role="img" aria-label="Photo of a person reading a business newspaper at a desk with a plant and a coffee mug"></section>
<div class="abs hero-ring"></div>
<div class="abs hero-disc">
  <div class="hero-title">Home Income<br>and Business Resources</div>
  <div class="hero-rule"></div>
  <p class="hero-text">Lorem Ipsum is simply dummy text of the printing and typesettin Lorem Ipsum has been the industry's standard dummy text</p>
  <span class="btn">Read More</span>
</div>

<section>
  <article class="abs feature" style="left:43px">
    <div class="feature-tab" role="img" aria-label="Illustration of a hand holding a house"><span></span></div>
    <h2>Home Income Resource Directory</h2>
    <p>Text: Find what you need, when you need it.The KelvaNest website directory is your one-stop pit for anything involved in making money from home marketing your business or finding a opportunity. Our modern, community supported directory will help a sensibl Lorem Ipsum is simply dummy text of the printing and typesettin Lorem Ipsum has been the industry's standard dummy text ever since the 1500s, when an unknown printer took a</p>
    <span class="btn">Read More</span>
  </article>
  <article class="abs feature" style="left:425px">
    <div class="feature-tab" role="img" aria-label="Illustration of a presentation board with a chart"><span></span></div>
    <h2>Advertising Benefits</h2>
    <p>Text: Everyone needs to advertise and we know just how to get your offer out to the right people. We have many methods including: Text ads, E-mail, Display, newsletter and even some old school methods available to make your next campaign a success. Advertise a website, a link text, full page circular or a small account manager that will handle everything Lorem Ipsum is simply dummy text of the printing and typesetting industry. dummy text ever</p>
    <span class="btn blue">Read More</span>
  </article>
  <article class="abs feature" style="left:806px">
    <div class="feature-tab" role="img" aria-label="Illustration of a hand receiving a coin"><span></span></div>
    <h2>Earning With KelvaNest</h2>
    <p>Text: Join KelvaNest and start earning money. When you share KelvaNest and lock in an advertiser or premium listing, we reward you. Build a downline at any of our listed sites when you share KelvaNest with NO extra work. Its all done for you.We also offer a of our is the printing and typesetting industry. Lorem Ipsum has been the industry's standard dummy text ever since the 1500s, when an unknown printer took a galley esetting industry. Lorem</p>
    <span class="btn">Read More</span>
  </article>
</section>

<main>
  <article class="abs post" style="top:1043px">
    <div class="post-photo" role="img" aria-label="Photo of a smiling woman in a pink blazer talking on the phone beside a laptop" style="background:linear-gradient(160deg,#3d5a2c 0%,#6f8a4a 35%,#d9b4b6 65%,#eee6e4 100%)"></div>
    <div class="post-body">
      <h3 class="post-title">Chronic Illness and Starting an<br>Exercise Regimen</h3>
      <div class="post-rule"></div>
      <div class="post-cat">Daily Living, Health</div>
      <p class="post-text">Your general health is intimately connected with the foods and drinks you put into your body. Each person is unique in what food or drink can trigger feeling unhealthy and rundown. It is very easy to lose track of which foods and drinks can be wreaking havoc with your health. A great way to do some detective work</p>
      <div class="post-meta">Written by &nbsp;<b>Mara Ellison</b>&nbsp; in &nbsp;<b>August 22, 2016</b></div>
      <div class="post-divider"></div>
      <span class="btn">Read More</span>
      <div class="post-stats">
        <span><svg width="13" height="11" viewBox="0 0 13 11"><path fill="#1893dd" d="M6.5 0C10 0 13 2 13 4.6S10 9.2 6.5 9.2c-.6 0-1.2 0-1.7-.2L1.5 11l.9-2.8C.9 7.4 0 6.1 0 4.6 0 2 3 0 6.5 0z"/></svg>05</span>
        <span><svg width="12" height="11" viewBox="0 0 12 11"><path fill="#1893dd" d="M6 11 .9 5.8A3.1 3.1 0 0 1 6 1.6a3.1 3.1 0 0 1 5.1 4.2z"/></svg>02</span>
      </div>
    </div>
  </article>

  <article class="abs post" style="top:1444px">
    <div class="post-photo" role="img" aria-label="Photo of a laptop keyboard and a car key on a desk" style="background:linear-gradient(150deg,#6f86a6 0%,#2d3e5c 40%,#1b2436 70%,#5c7392 100%)"></div>
    <div class="post-body">
      <h3 class="post-title">Chronic Illness and Starting an<br>Exercise Regimen</h3>
      <div class="post-rule"></div>
      <div class="post-cat">Daily Living, Health</div>
      <p class="post-text">Your general health is intimately connected with the foods and drinks you put into your body. Each person is unique in what food or drink can trigger feeling unhealthy and rundown. It is very easy to lose track of which foods and drinks can be wreaking havoc with your health. A great way to do some detective work</p>
      <div class="post-meta">Written by &nbsp;<b>Mara Ellison</b>&nbsp; in &nbsp;<b>August 22, 2016</b></div>
      <div class="post-divider"></div>
      <span class="btn blue">Read More</span>
      <div class="post-stats">
        <span><svg width="13" height="11" viewBox="0 0 13 11"><path fill="#1893dd" d="M6.5 0C10 0 13 2 13 4.6S10 9.2 6.5 9.2c-.6 0-1.2 0-1.7-.2L1.5 11l.9-2.8C.9 7.4 0 6.1 0 4.6 0 2 3 0 6.5 0z"/></svg>05</span>
        <span><svg width="12" height="11" viewBox="0 0 12 11"><path fill="#1893dd" d="M6 11 .9 5.8A3.1 3.1 0 0 1 6 1.6a3.1 3.1 0 0 1 5.1 4.2z"/></svg>02</span>
      </div>
    </div>
  </article>

  <article class="abs post" style="top:1838px">
    <div class="post-photo" role="img" aria-label="Photo of hands typing on a laptop at a wooden desk with a mug" style="background:linear-gradient(160deg,#6b3b22 0%,#a2663f 30%,#d8d7d5 60%,#f2f2f0 100%)"></div>
    <div class="post-body">
      <h3 class="post-title">Chronic Illness and Starting an<br>Exercise Regimen</h3>
      <div class="post-rule"></div>
      <div class="post-cat">Daily Living, Health</div>
      <p class="post-text">Your general health is intimately connected with the foods and drinks you put into your body. Each person is unique in what food or drink can trigger feeling unhealthy and rundown. It is very easy to lose track of which foods and drinks can be wreaking havoc with your health. A great way to do some detective work</p>
      <div class="post-meta">Written by &nbsp;<b>Mara Ellison</b>&nbsp; in &nbsp;<b>August 22, 2016</b></div>
      <div class="post-divider"></div>
      <span class="btn">Read More</span>
      <div class="post-stats">
        <span><svg width="13" height="11" viewBox="0 0 13 11"><path fill="#1893dd" d="M6.5 0C10 0 13 2 13 4.6S10 9.2 6.5 9.2c-.6 0-1.2 0-1.7-.2L1.5 11l.9-2.8C.9 7.4 0 6.1 0 4.6 0 2 3 0 6.5 0z"/></svg>05</span>
        <span><svg width="12" height="11" viewBox="0 0 12 11"><path fill="#1893dd" d="M6 11 .9 5.8A3.1 3.1 0 0 1 6 1.6a3.1 3.1 0 0 1 5.1 4.2z"/></svg>02</span>
      </div>
    </div>
  </article>
</main>

<aside class="abs sidebar">
  <div class="avatar" role="img" aria-label="Portrait photo of the site author"></div>
  <h2 class="side-h" style="top:172px">About Us</h2>
  <p class="side-text">Lorem Ipsum is simply dummy text of the printing and typesetting industry. Lorem Ipsum has been the industry's standard dummy text ever since the 1500s, when an wn printer took a galley of type and scram-bled it to</p>
  <h2 class="side-h" style="top:348px">Social Media</h2>
  <div class="side-rule" style="top:387px"></div>
  <div class="social"><span></span><span></span><span></span><span></span><span></span></div>
  <div class="follow">Follow Us</div>
  <h2 class="side-h" style="top:506px">Recent Posts</h2>
  <div class="side-rule" style="top:545px"></div>
  <div class="recent-photo" role="img" aria-label="Photo of a young woman in a sun hat blowing bubbles outdoors"></div>
  <div class="recent-title">Regular Exercise is a Natural Anti-Inflammatory</div>
  <div class="recent-date">August 22, 2016</div>
  <div class="pager">
    <span><svg width="8" height="10" viewBox="0 0 8 10"><path d="M6 1 2 5l4 4" stroke="#fff" stroke-width="2" fill="none"/></svg></span>
    <span><svg width="8" height="10" viewBox="0 0 8 10"><path d="m2 1 4 4-4 4" stroke="#fff" stroke-width="2" fill="none"/></svg></span>
  </div>
  <h2 class="side-h" style="top:836px">Hey Warriors, We Support You!</h2>
  <div class="promo">
    <h3>Advertising<br>Benefits</h3>
    <p>Action plan chronic chronic illness chronic illness pain chronic pain coping with a chronic illness depression employment energy failure fibro fibro-myalgia focus food diary functional medicine goal action plan goals inflammation invisible illness job job hunting life goals</p>
  </div>
</aside>

<div class="abs footer-rule"></div>
<footer class="abs footer">
  <div class="footer-social"><span></span><span></span><span></span></div>
  <a href="#">About Us</a><a href="#">Privacy Policy</a><a href="#">Terms of Use</a><a href="#">Advertise Us</a><a href="#">Help</a>
  <span class="copy">© 2017 Copyright</span>
</footer>

</body>
</html>
```